Corvath Insurance Stationery Design Project

We need a stationery design for business cards, letterhead and envelopes.

Please refer to attached brief for further information.

Business

```html
<!DOCTYPE html>
<html lang="en">
<head>
<meta charset="utf-8">
<title>Corvath Insurance Stationery</title>
<link href="https://fonts.googleapis.com/css2?family=Questrial&display=swap" rel="stylesheet">
<style>
  :root {
    --backdrop: #4168b5;
    --paper: #ffffff;
    --navy: #1d2d4a;
    --orange: #e8790f;
    --grey: #6d7580;
    --card-dark-a: #2c4470;
    --card-dark-b: #16233d;
  }
  * { margin: 0; padding: 0; box-sizing: border-box; }
  html, body { width: 1200px; height: 900px; overflow: hidden; }
  body {
    background: var(--backdrop);
    font-family: "Questrial", "Century Gothic", sans-serif;
    color: var(--navy);
    position: relative;
  }
  .sheet { position: absolute; background: var(--paper); }

  /* brand name lockup */
  .brand { position: absolute; display: flex; align-items: center; white-space: nowrap; }
  .brand-dot { width: 7px; height: 7px; border-radius: 50%; background: var(--orange); margin-right: 5px; flex: none; }
  .brand-name { font-weight: 400; color: var(--navy); letter-spacing: 0.2px; }
  .brand.on-dark .brand-name { color: #ffffff; }

  .rule { position: absolute; width: 1px; background: var(--navy); }
  .text { position: absolute; white-space: nowrap; }

  /* business card front */
  .card-front { left: 177px; top: 173px; width: 141px; height: 255px; }
  .card-front .brand { left: 16px; top: 26px; }
  .card-front .brand-name { font-size: 13px; }
  .card-name { left: 21px; top: 77px; font-size: 9px; font-weight: 700; color: var(--orange); }
  .card-name .role { color: var(--navy); }
  .card-front .rule { left: 21px; top: 98px; height: 86px; }
  .card-contact { left: 33px; top: 101px; font-size: 7px; line-height: 9px; color: var(--navy); }
  .card-contact .gap { height: 9px; }
  .card-web { left: 0; width: 141px; text-align: center; top: 195px; font-size: 8px; color: var(--orange); }
  .card-legal { left: 6px; width: 129px; top: 212px; font-size: 4px; line-height: 5px; text-align: center; color: var(--grey); white-space: normal; }

  /* business card back */
  .card-back {
    left: 334px; top: 173px; width: 140px; height: 257px;
    background: radial-gradient(ellipse at 50% 25%, var(--card-dark-a), var(--card-dark-b) 75%);
  }
  .card-back .brand { left: 13px; top: 112px; }
  .card-back .brand-name { font-size: 13px; }

  /* envelope */
  .envelope { left: 114px; top: 491px; width: 548px; height: 275px; }
  .envelope .brand { left: 25px; top: 33px; }
  .envelope .brand-name { font-size: 15px; }
  .envelope .rule { left: 63px; top: 82px; height: 40px; }
  .return-address { left: 67px; top: 83px; font-size: 8px; line-height: 9px; font-weight: 700; }
  .return-address .gap { height: 9px; }

  /* letterhead */
  .letterhead { left: 531px; top: 82px; width: 522px; height: 739px; }
  .letterhead .head-brand { left: 179px; top: 58px; }
  .letterhead .head-brand .brand-name { font-size: 19px; }
  .tagline { left: 229px; top: 101px; font-size: 10px; font-weight: 700; letter-spacing: 0.5px; }
  .footer-mark { position: absolute; left: 180px; top: 662px; width: 9px; height: 9px; border-radius: 50%; background: var(--orange); }
  .letterhead .rule { left: 214px; top: 661px; height: 58px; }
  .footer { left: 227px; top: 661px; font-size: 6px; line-height: 8px; color: var(--navy); }
  .footer .web { color: var(--orange); }
  .footer .legal { font-size: 4px; line-height: 5px; color: var(--grey); white-space: normal; width: 255px; margin-top: 2px; }
</style>
</head>
<body>

  <section class="sheet card-front" aria-label="Business card, front">
    <div class="brand"><span class="brand-dot"></span><span class="brand-name">Corvath Insurance</span></div>
    <div class="text card-name">DANA HOLLIS <span class="role">Director</span></div>
    <div class="rule"></div>
    <div class="text card-contact">
      <div>Level 4, 18 Harbour Rd</div>
      <div>Eastwick NSW 2071</div>
      <div>PO Box 412</div>
      <div>Eastwick NSW 2072</div>
      <div class="gap"></div>
      <div>T: (02) 5550 1234</div>
      <div>F: (02) 5550 1278</div>
      <div>M: 0400 555 219</div>
      <div>E: dhollis@corvathmail.com.au</div>
    </div>
    <div class="text card-web">www.corvathinsurance.com.au</div>
    <p class="text card-legal">Authorised Representative No. 000000. Issued under licence through a partner network. Advice is general only and does not consider your personal needs. Please read all product terms before acting.</p>
  </section>

  <section class="sheet card-back" aria-label="Business card, back">
    <div class="brand on-dark"><span class="brand-dot"></span><span class="brand-name">Corvath Insurance</span></div>
  </section>

  <section class="sheet envelope" aria-label="Envelope">
    <div class="brand"><span class="brand-dot"></span><span class="brand-name">Corvath Insurance</span></div>
    <div class="rule"></div>
    <div class="text return-address">
      <div>Corvath Insurance Holdings Pty Ltd</div>
      <div class="gap"></div>
      <div>PO Box 412</div>
      <div>Eastwick NSW 2072</div>
    </div>
  </section>

  <section class="sheet letterhead" aria-label="Letterhead">
    <div class="brand head-brand"><span class="brand-dot"></span><span class="brand-name">Corvath Insurance</span></div>
    <div class="text tagline">Business and Life Insurance Brokers and Advisers</div>
    <div class="footer-mark"></div>
    <div class="rule"></div>
    <div class="text footer">
      <div>Copyright 2012 Corvath Insurance Holdings Pty Ltd. All rights reserved.</div>
      <div>Level 4, 18 Harbour Rd, Eastwick NSW 2071; PO Box 412, Eastwick NSW 2072</div>
      <div>Ph: (02) 5550 1234; fax: (02) 5550 1278; email: info@corvathinsurance.com.au</div>
      <div class="web">www.corvathinsurance.com.au</div>
      <p class="legal">Corvath Insurance Holdings Pty Ltd is an authorised representative under a partner licence. Advice given is general in nature and does not account for individual objectives. Consider all disclosure documents before making any decision.</p>
    </div>
  </section>

</body>
</html>
```